Webdesign für Entwickler von onlinebasierten Terminformularen
Super Designs. Schnell und motiviert. Danke für die hervorragende Umsetzung und die Ideen!
Zielgruppe
Deutsch:
Wir sind ein Startup, das über die Seite Kalendrio.de zukünftig folgenden Service anbietet: Unternehmer können sehr flexibel (selbst) gestaltete Terminformulare erstellen und auf Ihrer Website einbinden. Kunden können dann diese Termine buchen und bekommen dann Erinnerungs-Mails und SMS.
Zielgruppe: Dienstleister wie Fotografen, Friseure, Versicherungsvertreter, Masseure, Restaurants, Arztpraxen. Also alle, die darauf angewiesen sind, dass vereinbarte Termine eingehalten werden und die die Terminvereinbarung vereinfachen wollen. Also weniger per Telefon, mehr über die eigene Website.
Englisch:
We are a start up, that is going to offer this services on the Website Kalendrio.de :
Companies can create highly flexible (self-designed) appointment forms and integrate them on their website. Customer can book appointments and will get an reminding email and SMS.
Target group: Service providers such as photographers, hairdressers, insurance agents, masseurs, restaurants, medical offices. So all those who depend on meeting agreed appointments and who want to simplify the appointment. Less by telephone, more over their own website.
Aufgabenstellung
Übersichtlichkeit, genug Weißraum, deutliche, große Überschriften, Seriös aber gerne frische Farben bei einzelnen Elementen (z.B. bei Icons oder bei Handlungsaufforderungs-Buttons), Trennlinien, Inhalte auf den Punkt.
Logo-Entwurf anbei (wird gerade hier über entwurfhafen.de ebenfalls erstellt/optimiert, siehe #817306) sagt das wesentliche aus.
Kalendrio soll also ein sehr nützliches Tool sein, das jeder schnell versteht. Daher muss auch die Website sehr übersichtlich und klar aufgebaut werden. Die wesentlichen Aussagen/Menüpunkte finden sich auf der Startseite (bzw. im Hauptmenü, siehe grober Entwurf anbei).
- frische Farben (z.B. grün, orange, gelb)
- seröse Farben/Grauwerte (z.B. blau, grau, schwarz)
- Hauptmenü/Metanavigation/Footer-Bereich
Das Design und das Teaser-Bild (Frau mit Hammer) auf dem Entwurf anbei (seite1_mit_teaser_entwurf2.jpg) sind nur als grobe Ideen (Richtung) zu verstehen. Die Startseite muss also keine Teaser-Bilder enthalten.
Der Entwurf anbei soll lediglich die ungefähre Richtung mit den angedachten Menüpunkten verdeutlichen.
Übersichtlich und modern finden wir z.B. https://talkroomly.example/de (viel Weißraum, farbige Icons, Infos übersichtlich dargeboten, lächelnde Gesichter) und übrigens auch https://www.entwurfhafen.example.
Bitte entwerfen Sie (erstmal) drei Seiten:
- Startseite
- Funktionen/Preis (Beispiel auf https://talkroomly.example/de/tools Und/oder in Tabellenform wie auf https://talkroomly.example/de/pricing/ siehe Content-Plan anbei)
- Über Kalendrio (Über uns, siehe Content-Plan anbei)
Der Content-Plan soll das Projekt verdeutlichen.
Anmerkung von unserem Programmierer: Praktisch wäre eine Basis auf Bootstrap. Dies ist aber keine Pflicht! Das Design/die Idee geht vor :-)
1zu1-Folgeaufträge (für dieses und andere Projekte im Bereich Webdesign, Flyer, CorporateDesign, Grafiken) sind sehr wahrsc..

```html
<!DOCTYPE html>
<html lang="de">
<head>
<meta charset="utf-8">
<title>Kalendrio Blog</title>
<link href="https://fonts.googleapis.com/css2?family=Nunito+Sans:wght@300;400;600;700&display=swap" rel="stylesheet">
<style>
:root{
  --green:#8cc04b;
  --slate:#6d777d;
  --slate-dark:#4f575d;
  --text:#5d676d;
  --muted:#9aa1a6;
  --faint:#d3d7da;
  --white:#ffffff;
}
*{box-sizing:border-box;margin:0;padding:0}
html,body{width:1200px;height:2616px;overflow:hidden}
body{font-family:"Nunito Sans",sans-serif;color:var(--text);background:var(--white);position:relative}
a{color:inherit;text-decoration:none}
.meta-bar{height:31px;background:var(--slate);display:flex;justify-content:flex-end;align-items:center;padding-right:217px;font-size:9px;color:var(--white);gap:10px}
.meta-bar .sep{width:1px;height:11px;background:rgba(255,255,255,.4)}
.main-nav{height:51px;display:flex;align-items:center;padding:0 214px 0 237px;border-bottom:1px solid #eceef0}
.brand{display:flex;align-items:center;gap:6px;font-size:24px;font-weight:700;color:var(--green);margin-right:26px}
.brand .mark{width:16px;height:16px;background:var(--slate)}
.main-nav .links{display:flex;gap:38px;font-size:10.5px}
.main-nav .links a.active{color:var(--green);border-bottom:2px solid var(--green);padding-bottom:7px;margin-top:9px}
.main-nav .account{margin-left:auto;display:flex;align-items:center;gap:20px;font-size:10.5px}
.btn-outline{border:1.5px solid var(--green);border-radius:16px;padding:7px 13px}
.hero{height:210px;background:var(--slate);color:var(--white);text-align:center;padding-top:74px}
.hero h1{font-size:26px;font-weight:700;margin-bottom:8px}
.hero p{font-size:16px;font-weight:300}
.category{position:absolute;left:214px;width:771px}
.category-head{display:flex;justify-content:space-between;align-items:flex-end;margin-bottom:11px}
.category-head h2{font-size:20px;font-weight:600;color:var(--text)}
.category-head a{font-size:9px;font-weight:700;color:var(--green)}
.grid{display:flex;gap:19px}
.card{width:179px}
.thumb{width:179px;height:117px;border-radius:3px}
.card h3{font-size:12.5px;font-weight:700;line-height:17px;margin-top:14px}
.date{font-size:9px;color:var(--faint);margin:8px 0 5px}
.excerpt{font-size:9px;line-height:17.5px;color:var(--muted)}
.row{display:flex;gap:19px;margin-bottom:25px}
.row .text{width:179px}
.row .text h3{margin-top:0}
.t1{background:linear-gradient(135deg,#7a6a5a,#c9b9a8 60%,#4c5258)}
.t2{background:linear-gradient(135deg,#2a3440,#5f6f7e 60%,#b7c2cc)}
.t3{background:linear-gradient(135deg,#cfd5da,#8c9097 60%,#30343a)}
.t4{background:linear-gradient(135deg,#3a4a5c,#6f88a3 60%,#c1ccd6)}
.t5{background:linear-gradient(135deg,#c8d2dc,#8796a5 55%,#3c4652)}
.t6{background:linear-gradient(135deg,#f4f4f6,#dcdde3 60%,#b6bcc8)}
.t7{background:linear-gradient(135deg,#dfe7ef,#9fb4c8 60%,#4f6070)}
.t8{background:linear-gradient(135deg,#e6e2dc,#a8b0b8 60%,#5b6b80)}
.t9{background:linear-gradient(135deg,#bcbcbc,#e8e8e8 60%,#8f8f8f)}
.t10{background:linear-gradient(135deg,#e8c89a,#a76b4a 55%,#3c2b24)}
.t11{background:linear-gradient(135deg,#e9ebee,#c8ccd3 60%,#9aa1ab)}
.t12{background:linear-gradient(135deg,#f6f6f6,#ececec 60%,#d8dcdc)}
.cta{position:absolute;top:1967px;left:0;width:1200px;height:400px;background:radial-gradient(ellipse at 70% 40%,#8a8a86,#5e5a55 45%,#3a3634 100%)}
.cta-content{position:absolute;top:2116px;left:0;width:1200px;text-align:center;color:var(--white)}
.cta-content h2{font-size:27px;font-weight:700;margin-bottom:10px}
.cta-content p{font-size:16px;font-weight:300;line-height:24px;width:420px;margin:0 auto 27px}
.btn-solid{display:inline-block;width:354px;height:49px;line-height:49px;background:var(--green);color:var(--white);font-size:12px;font-weight:700}
.footer-brand{position:absolute;top:2367px;left:0;width:1200px;height:67px;background:var(--slate);padding:22px 0 0 214px}
.footer-brand .brand{color:var(--white);font-size:22px}
.footer-brand .brand .mark{background:var(--white)}
.footer{position:absolute;top:2434px;left:0;width:1200px;height:182px;background:var(--slate-dark);color:var(--white);font-size:9.5px}
.copyright{position:absolute;left:214px;top:15px}
.lang{position:absolute;left:214px;top:50px;width:144px;height:30px;border:1px solid rgba(255,255,255,.6);border-radius:15px;padding:8px 20px}
.lang b{margin-left:12px}
.col{position:absolute;top:16px;line-height:17.5px}
.col h4{font-size:9.5px;font-weight:600;margin-bottom:7px}
.col a{display:block;color:#d9dde0}
.rating{position:absolute;left:799px;top:16px;width:184px}
.rating h4{font-size:9.5px;font-weight:600;margin-bottom:9px}
.rating p{font-size:8px;line-height:12px;color:#d9dde0;margin-bottom:14px}
.rating .btn-solid{width:184px;height:37px;line-height:37px;font-size:10px;text-align:center}
</style>
</head>
<body>
<div class="meta-bar"><a>Kontakt</a><span class="sep"></span><a>DE ⌄</a><span class="sep"></span><a>Zu Wertungsplatz wechseln</a></div>
<nav class="main-nav">
  <div class="brand"><span class="mark"></span>Kalendrio</div>
  <div class="links"><a class="active">Funktionen / Preis</a><a style="margin-top:0">Help-Center</a><a>Über Uns</a><a>Blog</a></div>
  <div class="account"><a>Login</a><a class="btn-outline">Konto erstellen</a></div>
</nav>
<header class="hero"><h1>Kalendrio Blog</h1><p>Lesen Sie mehr zu Uns und Kalendrio.</p></header>

<section class="category" style="top:355px">
  <div class="category-head"><h2>Technische News</h2><a>Alle News aus dieser Kategorie</a></div>
  <div class="grid">
    <article class="card"><div class="thumb t1" role="img" aria-label="Foto: Team im Büro am Tablet"></div><h3>Lorem Ipsum Dolor sit amet Kalendrio</h3><p class="date">vom 18.05.2018</p><p class="excerpt">Lorem ipsum dolor sit amet, consetetur sadipscing elitr, sed diam nonumy eirmod tempor invidunt ut labore et</p></article>
    <article class="card"><div class="thumb t2" role="img" aria-label="Foto: Programmcode auf Monitoren"></div><h3>Lorem Ipsum Dolor sit amet Kalendrio</h3><p class="date">vom 18.05.2018</p><p class="excerpt">Lorem ipsum dolor sit amet, consetetur sadipscing elitr, sed diam nonumy eirmod tempor invidunt ut labore et</p></article>
    <article class="card"><div class="thumb t3" role="img" aria-label="Foto: Hand am Tablet mit Diagramm"></div><h3>Lorem Ipsum Dolor sit amet Kalendrio</h3><p class="date">vom 18.05.2018</p><p class="excerpt">Lorem ipsum dolor sit amet, consetetur sadipscing elitr, sed diam nonumy eirmod tempor invidunt ut labore et</p></article>
    <article class="card"><div class="thumb t4" role="img" aria-label="Foto: Hand mit digitaler Oberfläche"></div><h3>Lorem Ipsum Dolor sit amet Kalendrio</h3><p class="date">vom 18.05.2018</p><p class="excerpt">Lorem ipsum dolor sit amet, consetetur sadipscing elitr, sed diam nonumy eirmod tempor invidunt ut labore et</p></article>
  </div>
</section>

<section class="category" style="top:689px">
  <div class="category-head"><h2>Kalendrio News</h2><a>Alle News aus dieser Kategorie</a></div>
  <div class="grid">
    <article class="card"><div class="thumb t5" role="img" aria-label="Foto: Geschäftsleute beim Handschlag"></div><h3>Lorem Ipsum Dolor sit amet Kalendrio</h3><p class="date">vom 18.05.2018</p><p class="excerpt">Lorem ipsum dolor sit amet, consetetur sadipscing elitr, sed diam nonumy eirmod tempor invidunt ut labore et</p></article>
    <article class="card"><div class="thumb t6" role="img" aria-label="Illustration: App-Entwicklung"></div><h3>Lorem Ipsum Dolor sit amet Kalendrio</h3><p class="date">vom 18.05.2018</p><p class="excerpt">Lorem ipsum dolor sit amet, consetetur sadipscing elitr, sed diam nonumy eirmod tempor invidunt ut labore et</p></article>
    <article class="card"><div class="thumb t7" role="img" aria-label="Foto: Team am Besprechungstisch"></div><h3>Lorem Ipsum Dolor sit amet Kalendrio</h3><p class="date">vom 18.05.2018</p><p class="excerpt">Lorem ipsum dolor sit amet, consetetur sadipscing elitr, sed diam nonumy eirmod tempor invidunt ut labore et</p></article>
    <article class="card"><div class="thumb t8" role="img" aria-label="Foto: Mann mit Tablet"></div><h3>Lorem Ipsum Dolor sit amet Kalendrio</h3><p class="date">vom 18.05.2018</p><p class="excerpt">Lorem ipsum dolor sit amet, consetetur sadipscing elitr, sed diam nonumy eirmod tempor invidunt ut labore et</p></article>
  </div>
</section>

<section class="category" style="top:1022px">
  <div class="category-head"><h2>Beiträge zu Terminvereinbarungen</h2><a>Alle News aus dieser Kategorie</a></div>
  <div class="grid">
    <article class="card"><div class="thumb t5" role="img" aria-label="Foto: Team bei Besprechung"></div><h3>Lorem Ipsum Dolor sit amet Kalendrio</h3><p class="date">vom 18.05.2018</p><p class="excerpt">Lorem ipsum dolor sit amet, consetetur sadipscing elitr, sed diam nonumy eirmod tempor invidunt ut labore et</p></article>
    <article class="card"><div class="thumb t9" role="img" aria-label="Foto: Kalenderblatt mit Termin-Notiz"></div><h3>Lorem Ipsum Dolor sit amet Kalendrio</h3><p class="date">vom 18.05.2018</p><p class="excerpt">Lorem ipsum dolor sit amet, consetetur sadipscing elitr, sed diam nonumy eirmod tempor invidunt ut labore et</p></article>
    <article class="card"><div class="thumb t10" role="img" aria-label="Foto: Frauen am Laptop im Gegenlicht"></div><h3>Lorem Ipsum Dolor sit amet Kalendrio</h3><p class="date">vom 18.05.2018</p><p class="excerpt">Lorem ipsum dolor sit amet, consetetur sadipscing elitr, sed diam nonumy eirmod tempor invidunt ut labore et</p></article>
    <article class="card"><div class="thumb t11" role="img" aria-label="Foto: Kalender mit Pinnnadeln"></div><h3>Lorem Ipsum Dolor sit amet Kalendrio</h3><p class="date">vom 18.05.2018</p><p class="excerpt">Lorem ipsum dolor sit amet, consetetur sadipscing elitr, sed diam nonumy eirmod tempor invidunt ut labore et</p></article>
  </div>
</section>

<section class="category" style="top:1356px">
  <div class="category-head" style="margin-bottom:26px"><h2>Weitere Beiträge</h2><a>Alle News aus dieser Kategorie</a></div>
  <div class="row">
    <div class="thumb t12" role="img" aria-label="Grafik: abstrakte Kacheln"></div>
    <div class="text"><h3>Lorem Ipsum Dolor sit amet Kalendrio</h3><p class="date">vom 18.05.2018</p><p class="excerpt">Lorem ipsum dolor sit amet, consetetur sadipscing elitr, sed diam nonumy eirmod tempor invidunt ut labore et</p></div>
    <div class="thumb t5" role="img" aria-label="Foto: Team bei Besprechung"></div>
    <div class="text"><h3>Lorem Ipsum Dolor sit amet Kalendrio</h3><p class="date">vom 18.05.2018</p><p class="excerpt">Lorem ipsum dolor sit amet, consetetur sadipscing elitr, sed diam nonumy eirmod tempor invidunt ut labore et</p></div>
  </div>
  <div class="row">
    <div class="thumb t10" role="img" aria-label="Foto: Frauen am Laptop"></div>
    <div class="text"><h3>Lorem Ipsum Dolor sit amet Kalendrio</h3><p class="date">vom 18.05.2018</p><p class="excerpt">Lorem ipsum dolor sit amet, consetetur sadipscing elitr, sed diam nonumy eirmod tempor invidunt ut labore et</p></div>
    <div class="thumb t7" role="img" aria-label="Foto: Kollegen am Schreibtisch"></div>
    <div class="text"><h3>Lorem Ipsum Dolor sit amet Kalendrio</h3><p class="date">vom 18.05.2018</p><p class="excerpt">Lorem ipsum dolor sit amet, consetetur sadipscing elitr, sed diam nonumy eirmod tempor invidunt ut labore et</p></div>
  </div>
  <div class="row">
    <div class="thumb t8" role="img" aria-label="Foto: Mann mit Tablet"></div>
    <div class="text"><h3>Lorem Ipsum Dolor sit amet Kalendrio</h3><p class="date">vom 18.05.2018</p><p class="excerpt">Lorem ipsum dolor sit amet, consetetur sadipscing elitr, sed diam nonumy eirmod tempor invidunt ut labore et</p></div>
    <div class="thumb t6" role="img" aria-label="Illustration: App-Entwicklung"></div>
    <div class="text"><h3>Lorem Ipsum Dolor sit amet Kalendrio</h3><p class="date">vom 18.05.2018</p><p class="excerpt">Lorem ipsum dolor sit amet, consetetur sadipscing elitr, sed diam nonumy eirmod tempor invidunt ut labore et</p></div>
  </div>
</section>

<div class="cta" role="img" aria-label="Unscharfes Foto: Hände an Laptop und Kaffeetasse"></div>
<div class="cta-content">
  <h2>Holen Sie sich jetzt Kalendrio</h2>
  <p>Profitieren Sie jetzt von Kalendrio und sichern Sie sich alle Vorteile. Verwalten Sie jetzt Ihre Termine.</p>
  <a class="btn-solid">Jetzt kostenlos Konto erstellen</a>
</div>

<div class="footer-brand"><div class="brand"><span class="mark"></span>Kalendrio</div></div>
<footer class="footer">
  <p class="copyright">© 2018 Alle Rechte vorbehalten</p>
  <div class="lang">Sprachauswahl <b>DE ⌄</b></div>
  <div class="col" style="left:493px"><h4>Sonstiges</h4><a>Home</a><a>Kontakt</a><a>Newsletter</a><a>Webinare</a></div>
  <div class="col" style="left:574px"><h4>Benutzer</h4><a>Login</a><a>Konto erstellen</a></div>
  <div class="col" style="left:671px"><h4>Rechtliches</h4><a>Impressum</a><a>AGB</a><a>Datenschutz</a><a>Sitemap</a></div>
  <div class="rating"><h4>Bewertungen durch Wertungsplatz</h4><p>Verknüpfen Sie jetzt Kalendrio mit Wertungsplatz.de und profitieren Sie von vertrauensvollen Usern und Transparenz.</p><a class="btn-solid">zu Wertungsplatz.de wechseln</a></div>
</footer>
</body>
</html>
```